Los Angeles based Demolition, Grading, and Structural concrete Contractor in need of a Sale brochure

We are a Los Angeles-based demolition, grading, and structural concrete contractor looking for a professionally designed sales brochure that represents our company and services. The brochure should be visually appealing, easy to read, and include the following:

-Company Logo: Prominently displayed to enhance brand identity.

-Services We Offer: A clear breakdown of our key services, including demolition, grading, and structural concrete work.

-Project Scope & Capabilities: A brief explanation of the type of projects we handle (residential, commercial, industrial).

-Pricing Information: Mention that demolition services start at $20,000. This price includes complete demolition of structure, safe debris removal and hauling, site preparation for new construction.

-Contact Information: Our phone number(818.562.7180), email(contact@brvbuildworksinc.example) , and website for potential clients to reach out.

The design should reflect the professionalism and strength of our industry, using a modern, clean layout with bold colors that align with construction and demolition themes. Images of past work or stock photos representing our services are encouraged.

Final deliverables should be print-ready (PDF) and digital-friendly formats. Looking forward to creative and impactful designs!

```html
<!DOCTYPE html>
<html lang="en">
<head>
<meta charset="utf-8">
<title>BRV Buildworks – Sales Flyer</title>
<link href="https://fonts.googleapis.com/css2?family=Oswald:wght@500;600&family=Roboto:wght@400;500&display=swap" rel="stylesheet">
<style>
  :root {
    --page-bg: #d2d2d2;
    --paper: #ffffff;
    --brand-blue: #1a74c4;
    --teal: #0f87ad;
    --steel-grey: #8a8b8f;
    --ink: #1d1d1f;
    --sand: #c6a279;
    --sand-dark: #a98459;
    --yard-green: #7d8a5e;
  }
  * { box-sizing: border-box; margin: 0; padding: 0; }
  html, body { width: 714px; height: 1200px; overflow: hidden; background: var(--page-bg); }
  .flyer {
    position: absolute; left: 12px; top: 148px;
    width: 663px; height: 868px;
    background: var(--paper);
    transform: scale(1.0407); transform-origin: 0 0;
    overflow: hidden;
    font-family: "Roboto", Arial, sans-serif; color: var(--ink);
    box-shadow: 0 2px 6px rgba(0,0,0,.2);
  }
  .shapes { position: absolute; inset: 0; }
  .brand { position: absolute; left: 38px; top: 62px; display: flex; align-items: center; gap: 10px; }
  .brand-mark { width: 26px; height: 26px; background: var(--brand-blue); }
  .brand-name { font-family: "Oswald", sans-serif; font-weight: 600; font-size: 30px; color: var(--brand-blue); letter-spacing: 1px; text-transform: uppercase; }
  .headline {
    position: absolute; left: 38px; top: 208px;
    font-family: "Oswald", sans-serif; font-weight: 600; font-size: 33px; line-height: 40px;
    color: var(--brand-blue); letter-spacing: -.3px;
  }
  .intro { position: absolute; left: 39px; top: 304px; width: 420px; font-size: 12px; line-height: 15.5px; }
  .services { position: absolute; left: 38px; top: 394px; display: flex; gap: 10px; }
  .service { width: 188px; }
  .service-photo { width: 188px; height: 120px; background: linear-gradient(180deg, #9fae8a 0%, var(--yard-green) 45%, #b89d70 100%); }
  .service-title { margin-top: 10px; font-family: "Oswald", sans-serif; font-weight: 600; font-size: 17px; color: var(--teal); }
  .service-desc { margin-top: 3px; font-size: 9.6px; line-height: 12px; width: 180px; }
  .pricing { position: absolute; left: 40px; top: 626px; color: #fff; font-family: "Oswald", sans-serif; }
  .pricing-title { font-weight: 600; font-size: 22px; line-height: 28px; }
  .pricing-sub { font-weight: 500; font-size: 15px; margin-top: 2px; }
  .includes { position: absolute; left: 355px; top: 617px; list-style: none; color: #fff; font-size: 13px; font-weight: 500; }
  .includes li { height: 23px; display: flex; align-items: center; gap: 8px; }
  .includes svg { width: 14px; height: 14px; }
  .contact { position: absolute; left: 38px; top: 757px; color: #fff; }
  .contact-title { font-family: "Oswald", sans-serif; font-weight: 600; font-size: 19px; }
  .contact-phone { font-size: 16px; font-weight: 500; margin-top: 6px; letter-spacing: .3px; }
  .contact-line { font-size: 12.5px; margin-top: 4px; }
  .scope { position: absolute; left: 287px; top: 733px; width: 350px; }
  .scope-title { font-family: "Oswald", sans-serif; font-weight: 600; font-size: 19px; color: var(--teal); }
  .scope-text { margin-top: 8px; font-size: 10.6px; line-height: 15px; }
</style>
</head>
<body>
<div class="flyer">
  <svg class="shapes" viewBox="0 0 663 868" width="663" height="868">
    <defs>
      <linearGradient id="siteTones" x1="0" y1="0" x2="1" y2="1">
        <stop offset="0" stop-color="var(--sand)"/>
        <stop offset="1" stop-color="var(--sand-dark)"/>
      </linearGradient>
    </defs>
    <polygon points="196,0 663,0 663,378 240,158" fill="url(#siteTones)" role="img" aria-label="Photo of an excavator grading a dirt site"/>
    <polygon points="245,156 268,156 663,372 663,396" fill="var(--teal)"/>
    <polygon points="0,668 240,808 260,830 245,860 230,868 0,868" fill="var(--teal)"/>
    <polygon points="0,603 308,603 330,653 308,703 0,703" fill="var(--steel-grey)"/>
    <polygon points="316,603 663,603 663,703 316,703 338,653" fill="var(--teal)"/>
    <polygon points="0,665 70,703 0,703" fill="var(--teal)"/>
  </svg>

  <div class="brand"><span class="brand-mark"></span><span class="brand-name">BRV Buildworks</span></div>

  <h1 class="headline">Built for Strength,<br>Engineered for Success</h1>
  <p class="intro">BRV Buildworks Inc. is a trusted demolition, grading, and structural concrete contractor serving Los Angeles and beyond. With years of experience in the industry, we bring precision, efficiency, and safety to every project—whether residential, commercial, or industrial.</p>

  <div class="services">
    <div class="service">
      <div class="service-photo" role="img" aria-label="Photo of an excavator clearing a demolition site"></div>
      <h2 class="service-title">Demolition</h2>
      <p class="service-desc">Safe, efficient, and complete structure removal, including debris hauling.</p>
    </div>
    <div class="service">
      <div class="service-photo" role="img" aria-label="Photo of an excavator grading a site"></div>
      <h2 class="service-title">Grading</h2>
      <p class="service-desc">Site preparation for new builds, leveling, excavation, and soil stabilization.</p>
    </div>
    <div class="service">
      <div class="service-photo" role="img" aria-label="Photo of an excavator on a concrete job site"></div>
      <h2 class="service-title">Structural Concrete</h2>
      <p class="service-desc">Foundations, retaining walls, slabs, and reinforced concrete work.</p>
    </div>
  </div>

  <div class="pricing">
    <div class="pricing-title">Transparent Pricing</div>
    <div class="pricing-sub">Demolition services start at $20,000</div>
  </div>

  <ul class="includes">
    <li><svg viewBox="0 0 14 14"><path d="M2 7.5 L5.5 11 L12 3.5" fill="none" stroke="#fff" stroke-width="2.4"/></svg>Complete structure removal</li>
    <li><svg viewBox="0 0 14 14"><path d="M2 7.5 L5.5 11 L12 3.5" fill="none" stroke="#fff" stroke-width="2.4"/></svg>Safe debris removal &amp; hauling</li>
    <li><svg viewBox="0 0 14 14"><path d="M2 7.5 L5.5 11 L12 3.5" fill="none" stroke="#fff" stroke-width="2.4"/></svg>Site preparation for new construction</li>
  </ul>

  <div class="contact">
    <div class="contact-title">Call Us</div>
    <div class="contact-phone">818.562.7180</div>
    <div class="contact-line">contact@brvbuildworksinc.example</div>
    <div class="contact-line">www.brvbuildworksinc.example</div>
  </div>

  <div class="scope">
    <h2 class="scope-title">Project Scope &amp; Capabilities</h2>
    <p class="scope-text">We handle projects of all sizes, from small-scale residential demolitions to large commercial and industrial site preparations. Our skilled team ensures compliance with local regulations and industry best practices, delivering quality work on time and within budget.</p>
  </div>
</div>
</body>
</html>
```